Engineering Proposal Cover and Page Dividers

We are an engineering firm in Chicago, IL called VERANTH. (www.veranthpartners.example), We often submit on proposals and need a cover sheet and divider pages in order to make our submittals stand out. The attached information is required on the cover, as well as the client's logo, our logo, and a photograph or two. The Cover should be modifiable for use with different clients and/or proposal requests. Divider pages need to be modifiable but flow with the design of the cover and include a space to include text such as (Section 1: Cover Letter).
Target Market(s)
Government Agencies
Industry/Entity Type
Engineering
Font styles to use
Requirements
Must have
- Required information included in attached document. Modifiable file type (preferably InDesign).
Nice to have
- Should look professional, not for general consumption, but government agencies.

```html
<!DOCTYPE html>
<html lang="en">
<head>
<meta charset="utf-8">
<title>Section 2: Cost — VERANTH</title>
<link rel="stylesheet" href="https://fonts.googleapis.com/css2?family=Inter:wght@700;800&display=swap">
<style>
  :root {
    --brand-navy: #1b3f78;
    --divider-white: #ffffff;
    --soil-dark: #4a3f34;
    --soil-mid: #7a6a58;
    --soil-light: #a89a88;
  }
  html, body {
    margin: 0;
    padding: 0;
    width: 927px;
    height: 1200px;
    overflow: hidden;
    background: var(--divider-white);
  }
  .divider-page {
    position: relative;
    width: 927px;
    height: 1200px;
    font-family: "Inter", "Helvetica Neue", Arial, sans-serif;
  }
  .header-photo {
    position: absolute;
    left: 0;
    top: 0;
    width: 927px;
    height: 112px;
    background: linear-gradient(90deg, var(--soil-mid) 0%, var(--soil-dark) 30%, #2a2a2e 45%, var(--soil-dark) 60%, var(--soil-light) 85%, var(--soil-mid) 100%);
  }
  .brand-name {
    position: absolute;
    top: 36px;
    left: 0;
    width: 927px;
    margin: 0;
    text-align: center;
    color: var(--divider-white);
    font-weight: 800;
    font-size: 48px;
    letter-spacing: -0.5px;
    line-height: 1;
  }
  .section-panel {
    position: absolute;
    left: 0;
    top: 122px;
    width: 927px;
    height: 1078px;
    background: var(--brand-navy);
  }
  .section-title {
    position: absolute;
    left: 0;
    top: 510px;
    width: 927px;
    margin: 0;
    text-align: center;
    color: var(--divider-white);
    font-weight: 700;
    font-size: 98px;
    line-height: 121px;
    letter-spacing: -1px;
  }
</style>
</head>
<body>
  <main class="divider-page">
    <div class="header-photo" role="img" aria-label="Photograph of an excavated trench with a wrapped pipeline laid in soil"></div>
    <p class="brand-name">VERANTH</p>
    <section class="section-panel"></section>
    <h1 class="section-title">Section 2:<br>Cost</h1>
  </main>
</body>
</html>
```